designing a website for a vacation beach house rental

We are buying a vacation rental on an awesome beach on the Isle of Palms in South Carolina. The closing is not until November 30 so we will only have the photos from the current home and we can change the photos once we move our furniture in. We want the website to be exciting and interactive and for people to be able to go to a facebook page (that needs to be created) and the name of the beach house needs to be created (the address is 47 Tidewater Lane, Isle of Palms. We need to be able to take this site and add it to STYX and NookSpot and Bay Q&T and other travel sites. We need the person that clicks on it to be hooked from the first second. We think this one is pretty good but we want ours way better http://driftwoodcovehouse.example/ The price per week will be $7200 so the website needs to be elegant, stunning, all inclusive, retreat, relaxing, friends and family, eating together, amazing food town, beaches, golf, cocktails, wine, restaurants, history, architecture, opulence, Look up Charleston, SC to get an idea of what the area is all about. Top Chefs and top wines.

Target Market(s)

Upper class families with children; classy dressing; golfers; foodies; wine lovers; in shaper beach goers living the dream of a gorgeous beach house with friends and family at the pool, eating together, beach together, cooking together, playing games, walking on the beach, running on the beach, watching the sunset on the beach

Industry/Entity Type

House

Logo Text

the look and feel of an upper class family on vacation in an exclusive resort

Number of Pages Required

5+ page

Font styles to use
Serif

Requirements
Must have
• Lots of photos and movement; easy for me to update is a MUST; easy for a guest to register for staying; a calendar that will update automatically when someone pays; ability to take credit cards and CoinLoop; guest book; keep up with the number of visits; all of the bells and whistles of the most modern websites; also works on any device like ZPhone or ZSlate or any smartphone

```html
<!DOCTYPE html>
<html lang="en">
<head>
<meta charset="utf-8">
<title>Driftwood Cove House — Isle of Palms</title>
<link rel="stylesheet" href="https://fonts.googleapis.com/css2?family=Roboto:ital,wght@0,300;0,400;0,500;1,300&family=Open+Sans:ital,wght@0,400;1,400&display=swap">
<style>
:root{
  --ink:#222;
  --muted:#9a9a9a;
  --body:#333;
  --orange:#f5a400;
  --night:#0d0d0d;
  --white:#fff;
  --panel:rgba(15,15,15,.88);
  --line:#555;
}
*{box-sizing:border-box;margin:0;padding:0}
html,body{width:1200px;height:3186px;overflow:hidden}
body{position:relative;font-family:"Roboto",Arial,sans-serif;font-weight:300;color:var(--body);background:var(--white)}
.abs{position:absolute}

/* nav */
.topbar{left:0;top:0;width:1200px;height:47px;background:rgba(0,0,0,.92);z-index:5}
.brand{left:30px;top:15px;color:var(--orange);font-size:15px;font-weight:400;display:flex;align-items:center;gap:7px}
.brand i{width:14px;height:14px;border-radius:50%;background:var(--orange);display:block}
.menu a{position:absolute;top:16px;color:var(--white);font-size:13px;text-decoration:none;font-weight:400}
.menu a.active{color:var(--orange)}
.menu a.active::after{content:"";position:absolute;left:-10px;right:-10px;top:28px;height:2px;background:var(--orange)}
.book{left:1096px;top:10px;width:88px;height:29px;border-radius:15px;background:var(--orange);color:var(--white);font-size:12px;font-weight:500;display:flex;align-items:center;justify-content:center}

/* hero */
.hero{left:0;top:0;width:1200px;height:675px;background:
  linear-gradient(180deg,#1b1610 0%,#5a3a16 22%,#c7781f 38%,#f0a23a 43%,#8a4f17 47%,#2b2118 55%,#1d1a17 75%,#0f0f0f 100%)}
.arrow{width:30px;height:30px;border-radius:50%;display:flex;align-items:center;justify-content:center}
.arrow svg{width:10px;height:10px}
.hero-arrow.l{background:rgba(255,140,0,.55)}
.hero-arrow.r{background:#111}
.contact{left:701px;top:104px;width:374px;height:457px;background:var(--panel);border-radius:4px;color:var(--white)}
.contact h2{position:absolute;left:0;right:0;top:22px;text-align:center;font-size:22px;font-weight:300}
.contact .sub{position:absolute;left:0;right:0;top:56px;text-align:center;font-size:13px;color:#ccc}
.field{position:absolute;left:8px;right:8px;font-size:11px;color:#ccc;border-bottom:1px solid var(--line);padding-bottom:6px}
.field.name label{color:var(--orange)}
.field .val{display:block;color:var(--white);margin-top:4px;font-size:12px}
.question{left:8px;top:222px;width:358px;height:181px;border:1px solid var(--line);border-radius:3px}
.submit{left:276px;top:412px;width:86px;height:32px;background:var(--orange);border-radius:3px;font-size:11px;font-weight:500;display:flex;align-items:center;justify-content:center}
.mouse{left:588px;top:600px;width:22px;height:34px;border:2px solid #aaa;border-radius:11px}
.mouse::after{content:"";position:absolute;left:8px;top:6px;width:2px;height:7px;background:#aaa}

/* features */
.side-arrow{background:#eee}
.feature{width:300px;text-align:center;color:#cfcfcf}
.feature .label{font-size:20px;margin-top:6px}
.feature.main{color:var(--ink)}
.feature.main .label{font-size:30px;font-weight:400;margin-top:4px}
.feature .note{font-size:10px;font-style:italic;color:#888;line-height:15px;margin-top:8px}
.feature .link{font-size:11px;color:var(--orange);margin-top:6px}

/* sliders */
.slider{left:0;width:1200px;height:482px}
.slider.surf{top:977px;background:linear-gradient(180deg,#e9a95c 0%,#d88c2f 40%,#7a5430 80%,#4a3a2c 100%)}
.slider.sunset{top:1965px;height:484px;background:linear-gradient(180deg,#5a1a10 0%,#b3451f 40%,#8b2f17 70%,#3a120c 100%)}
.card{left:110px;width:988px;height:302px;background:var(--white);border-radius:4px;box-shadow:0 6px 24px rgba(0,0,0,.25)}
.photo{border:8px solid var(--white);box-shadow:0 8px 28px rgba(0,0,0,.35)}
.card h3{position:absolute;font-size:29px;font-weight:300;color:var(--ink)}
.card p{position:absolute;width:370px;font-family:"Open Sans",Arial,sans-serif;font-style:italic;font-size:14px;line-height:22px;color:var(--muted)}
.pill{position:absolute;width:110px;height:34px;border:1.5px solid var(--orange);border-radius:17px;color:var(--orange);font-size:12px;display:flex;align-items:center;justify-content:center}
.dots{display:flex;gap:6px;align-items:center}
.dots i{width:5px;height:5px;border-radius:50%;background:rgba(255,255,255,.8);display:block}
.dots i.on{background:var(--white);width:7px;height:7px}

/* history */
.history-title{left:0;width:1200px;top:1496px;text-align:center;font-size:29px;font-weight:300;color:var(--ink);letter-spacing:.5px}
.history-title b{font-weight:400}
.history-text{left:32px;top:1582px;width:688px;font-size:15px;line-height:19.5px;text-align:justify;color:var(--body)}
.history-text p{margin-bottom:13px}
.history-more{color:var(--orange);font-size:13px}
.history-pic{left:743px;top:1593px;width:429px;height:287px;background:linear-gradient(180deg,#3a1c3a 0%,#a33a2a 35%,#e0602a 50%,#5a2a2c 65%,#2a2230 100%)}

/* testimonial */
.quote{left:230px;top:2462px;width:740px;text-align:center;font-size:14.5px;line-height:20px;color:#444}
.guest{left:0;width:1200px;top:2616px;text-align:center;font-size:15px;font-weight:400;color:var(--ink)}
.quote-dots{left:574px;top:2690px}
.quote-dots i{background:#ccc}
.quote-dots i.on{background:var(--orange)}

/* golf */
.golf{left:0;top:2708px;width:1200px;height:312px;background:linear-gradient(180deg,#5f86b8 0%,#a9c2dc 35%,#6d7e58 55%,#4d6a2e 75%,#3d5a24 100%)}
.golf-quote{position:absolute;left:0;width:1200px;top:100px;text-align:center;color:rgba(255,255,255,.92);font-size:38px;font-weight:300}
.golf-cite{position:absolute;left:0;width:1200px;top:152px;text-align:center;color:rgba(255,255,255,.9);font-size:15px;font-style:normal}
.social{width:16px;height:16px;border-radius:50%;background:#cfcfcf}
.up{left:1164px;top:2954px;width:16px;height:16px;background:rgba(0,0,0,.35)}

/* footer */
.footer{left:0;top:3020px;width:1200px;height:166px;background:var(--night);color:#bbb;font-size:10px;line-height:22px}
.footer h4{font-size:10px;font-weight:500;color:var(--white);letter-spacing:.5px}
.footer .col{position:absolute;top:16px}
.footer .col span{display:block}
.footer .col span.active{color:var(--orange)}
.copy{left:0;width:1200px;top:3168px;text-align:center;color:#777;font-size:8px}
</style>
</head>
<body>

<section class="abs hero" role="img" aria-label="Photo of the sun setting over the sea from the beach"></section>
<header class="abs topbar">
  <div class="abs brand"><i></i>Driftwood Cove House</div>
  <nav class="menu">
    <a style="left:700px">Home</a>
    <a style="left:803px">About</a>
    <a style="left:890px">Things to Do</a>
    <a class="active" style="left:1002px">Contact Us</a>
  </nav>
  <div class="abs book">Book Now</div>
</header>
<div class="abs arrow hero-arrow l" style="left:38px;top:321px"><svg viewBox="0 0 10 10"><path d="M7 1 3 5 7 9" fill="none" stroke="#fff" stroke-width="1.6"/></svg></div>
<div class="abs arrow hero-arrow r" style="left:1130px;top:321px"><svg viewBox="0 0 10 10"><path d="M3 1 7 5 3 9" fill="none" stroke="#fff" stroke-width="1.6"/></svg></div>
<form class="abs contact">
  <h2>Do you have any questions ?</h2>
  <div class="sub">Feel free to ask</div>
  <div class="field name" style="top:98px"><label>Name</label><span class="val">Rory Lin|</span></div>
  <div class="field" style="top:158px"><label>Email</label></div>
  <div class="field" style="top:202px;border:0"><label>Your Question</label></div>
  <div class="abs question"></div>
  <div class="abs submit">SUBMIT</div>
</form>
<div class="abs mouse"></div>

<section class="features">
  <div class="abs arrow side-arrow" style="left:38px;top:805px"><svg viewBox="0 0 10 10"><path d="M7 1 3 5 7 9" fill="none" stroke="#333" stroke-width="1.6"/></svg></div>
  <div class="abs arrow side-arrow" style="left:1132px;top:805px"><svg viewBox="0 0 10 10"><path d="M3 1 7 5 3 9" fill="none" stroke="#333" stroke-width="1.6"/></svg></div>
  <div class="abs feature" style="left:107px;top:776px">
    <svg width="34" height="40" viewBox="0 0 34 40"><path d="M9 12a8 8 0 1 1 12 7c-3 2-4 3-4 7" fill="none" stroke="#cfcfcf" stroke-width="2"/><circle cx="17" cy="34" r="2" fill="#cfcfcf"/></svg>
    <div class="label" style="margin-top:0">FAQ</div>
  </div>
  <div class="abs feature main" style="left:451px;top:758px">
    <svg width="52" height="52" viewBox="0 0 56 56"><circle cx="26" cy="26" r="22" fill="none" stroke="#f5a400" stroke-width="3"/><line x1="42" y1="42" x2="50" y2="50" stroke="#f5a400" stroke-width="3"/><text x="26" y="35" text-anchor="middle" font-family="Roboto,Arial,sans-serif" font-size="26" font-weight="500" fill="#f5a400">$</text></svg>
    <div class="label">RATES</div>
    <div class="note">Rates from season to season ,<br>If you are looking for the rates please click the below link.</div>
    <div class="link">View Rates</div>
  </div>
  <div class="abs feature" style="left:799px;top:780px">
    <svg width="40" height="36" viewBox="0 0 40 36"><rect x="2" y="5" width="36" height="29" fill="none" stroke="#cfcfcf" stroke-width="2"/><line x1="2" y1="12" x2="38" y2="12" stroke="#cfcfcf" stroke-width="2"/><path d="M8 17h4M15 17h4M22 17h4M29 17h4M8 23h4M15 23h4M22 23h4M29 23h4M8 29h4M15 29h4" stroke="#cfcfcf" stroke-width="3"/><path d="M10 1v6M30 1v6" stroke="#cfcfcf" stroke-width="2"/></svg>
    <div class="label" style="margin-top:4px">CALENDAR</div>
  </div>
</section>

<section class="abs slider surf" role="img" aria-label="Blurred beach backdrop at sunset">
  <div class="abs card" style="top:89px">
    <h3 style="left:597px;top:40px">Surfing in South Carolina</h3>
    <p style="left:597px;top:90px">You can enjoy a lot in south carolina beach . Most favorite thing in this spot is surfing, water sports, campfire and lot more.</p>
    <div class="pill" style="left:597px;top:194px">View Photos</div>
  </div>
  <div class="abs photo" role="img" aria-label="Photo of a surfer holding a board on the shore at sunset" style="left:134px;top:55px;width:516px;height:370px;background:linear-gradient(180deg,#f2c471 0%,#e9a84a 45%,#b07838 65%,#6b4a2c 100%)"></div>
  <div class="abs arrow" style="left:38px;top:223px;background:rgba(245,164,0,.7)"><svg viewBox="0 0 10 10"><path d="M7 1 3 5 7 9" fill="none" stroke="#fff" stroke-width="1.6"/></svg></div>
  <div class="abs arrow" style="left:1132px;top:223px;background:#8a3a1a"><svg viewBox="0 0 10 10"><path d="M3 1 7 5 3 9" fill="none" stroke="#fff" stroke-width="1.6"/></svg></div>
  <div class="abs dots" style="left:574px;top:460px"><i class="on"></i><i></i><i></i><i></i></div>
</section>

<section class="history">
  <h2 class="abs history-title">HISTORY OF <b>ISLE OF PALMS</b></h2>
  <div class="abs history-text">
    <p>Originally named Hunting Island and then Long Island, it's thought to be at least 25,000 years old, and first inhabited by the indigenous Seewee Indians. The Seewees were said to have greeted the first English settlers to the area by swimming to the ships and carrying the travelers to shore. Whatever contributions the English made to the Seewees reportedly inspired some of them to try and reach England in their canoes-all lost at sea in storms.</p>
    <p>Legend has it that the only other occupants of the island were the pirates who buried their treasures for safekeeping in the deserted dunes and woods, although none has been found so far.</p>
    <p style="margin-bottom:6px">During the Revolutionary War a British Army contingent of 2,500 men attempted to raid a colonial encampment on adjacent Sullivan's Island. Many men drowned and the attack failed when the force attempted to cross the treacherous waters of the Breach Inlet between the two islands. The area was of significance again during the Civil War, as a point of departure for the CSS Hunley, the first submarine to sink an enemy vessel. After successfully sinking the USS Housatonic, the Hunley and her crew were lost at sea, probably as a result of the encounter with the Union ship. Amazingly, the wreck of the Hunley was recently discovered offshore of Sullivan's Island, and will soon be recovered for posterity.</p>
    <span class="history-more">Read more</span>
  </div>
  <div class="abs history-pic" role="img" aria-label="Photo of a fishing pier at sunset"></div>
</section>

<section class="abs slider sunset" role="img" aria-label="Blurred red sunset backdrop">
  <div class="abs card" style="top:91px">
    <h3 style="left:45px;top:40px">Isle of Palms Sunset</h3>
    <p style="left:45px;top:90px;width:300px">In this spot you can enjoy a sunset in a new dimension. We have a covered deck here you can have wine, tea and you can watch the sun set from the house.</p>
    <div class="pill" style="left:45px;top:194px">View Photos</div>
  </div>
  <div class="abs photo" role="img" aria-label="Photo of a pier stretching into the sea under a red sky" style="left:550px;top:59px;width:516px;height:363px;background:linear-gradient(180deg,#4a0f0c 0%,#b22a14 35%,#e04a1c 50%,#7a1e12 65%,#2a0c0a 100%)"></div>
  <div class="abs arrow" style="left:38px;top:223px;background:#1a0806"><svg viewBox="0 0 10 10"><path d="M7 1 3 5 7 9" fill="none" stroke="#fff" stroke-width="1.6"/></svg></div>
  <div class="abs arrow" style="left:1132px;top:223px;background:#1a0806"><svg viewBox="0 0 10 10"><path d="M3 1 7 5 3 9" fill="none" stroke="#fff" stroke-width="1.6"/></svg></div>
  <div class="abs dots" style="left:574px;top:462px"><i class="on"></i><i></i><i></i><i></i></div>
</section>

<section class="testimonial">
  <p class="abs quote">"Where to begin? Everything about this condo was lovely. The location, the owners, the home itself. Everything was in top repair, spotless and current. We were delighted with it all. The description of the home was entirely accurate but it was even in person."</p>
  <div class="abs guest">Guest, Brazil</div>
  <div class="abs dots quote-dots"><i class="on"></i><i></i><i></i><i></i><i></i></div>
</section>

<section class="abs golf" role="img" aria-label="Photo of a golfer swinging on a green course lined with trees">
  <div class="golf-quote">“Easy to reach South Carolina Golf Course ”</div>
  <div class="golf-cite">Dale Morrow, California</div>
</section>
<div class="abs up"><svg width="16" height="16" viewBox="0 0 16 16"><path d="M4 10 8 6 12 10" fill="none" stroke="#fff" stroke-width="1.5"/></svg></div>
<div class="abs social" style="left:1146px;top:2996px"></div>
<div class="abs social" style="left:1170px;top:2996px"></div>

<footer class="abs footer">
  <div class="col" style="left:110px">
    <h4>ADDRESS</h4>
    <span style="line-height:14px;margin-top:4px">47 Tidewater Lane,<br>Isle of Palms, SC 29451.</span>
    <span style="margin-top:10px;line-height:14px">Host Desk</span>
    <span style="line-height:18px">+00-55501-0000</span>
  </div>
  <div class="col" style="left:408px">
    <h4>CATEGORIES</h4>
    <span>Beach</span><span>Charleston</span><span>Food</span><span>Golf</span>
  </div>
  <div class="col" style="left:512px;top:38px"><span>History</span><span>Holidays</span><span>How To</span><span>Isle of Palms</span></div>
  <div class="col" style="left:620px;top:38px"><span>Local Information</span><span>News</span><span>News Letter</span><span>Our Guest Book</span></div>
  <div class="col" style="left:735px;top:38px"><span>South Carolina</span><span>Tours</span><span>Vacational Rental</span><span>Videos</span></div>
  <div class="col" style="left:1032px">
    <h4>PAGES</h4>
    <span>Home</span><span>About</span><span>Things to Do</span><span class="active">Contact Us</span>
  </div>
</footer>
<div class="abs copy">© Copyright - Driftwood Cove House Isle of Palms, South Carolina</div>

</body>
</html>
```